ORBIT Freight Lane Inc is a shipping company focusing on small parcel ecommerce shipments. Parcels shipments like you would receive from Marketvale or Tradowen. We have amazing shipping rates for both domestic and international shipping. We will offer a full service solution with tracking of the parcel from beginning to end customer. We will employ state of the art technology in our shipping solution and also provide an easy to use interface that integrates with Cartlofter and the other top shipping platforms.

Target Market(s)

ecommerce shipping companies, marketvale sellers, small businesses, 3PL's

Coding

Coded - Design and coding required

Number of Pages Required

3 page

Requirements
Must have
• A login page which takes you to our dashboard interface
Package tracking on UI page
Nice to have
• A technology look and feel. The UX of the site should make the viewer feel that they are using the best most technologically advanced shipping solution on the market

We will also be tying this service as a value add to our sister company www.zelnor-example.com They should not look the same as they are separate companies, but would be nice if they had a similar flare
Should not have
• Warehouse 3PL feel with people delivering boxes. We do not deliver and are not a 3PL, we are a technological platform for shipping, specializing in international parcel rates.

```html
<!DOCTYPE html>
<html lang="en">
<head>
<meta charset="utf-8">
<title>ORBIT Freight Lane — Sign In</title>
<link rel="stylesheet" href="https://fonts.googleapis.com/css2?family=Outfit:wght@300;400;500;600&display=swap">
<style>
  :root {
    --blue-deep: #1b5bd3;
    --blue-mid: #2a7fd0;
    --teal: #22b2bc;
    --accent: #36d1c9;
    --white: #ffffff;
    --ink: #111111;
    --field-border: #cfcfcf;
    --placeholder: #555555;
  }
  * { box-sizing: border-box; margin: 0; padding: 0; }
  html, body {
    width: 1200px;
    height: 675px;
    overflow: hidden;
    background: var(--white);
    font-family: "Outfit", sans-serif;
  }
  .login-page {
    position: relative;
    width: 1200px;
    height: 675px;
    display: flex;
  }
  .hero {
    position: relative;
    width: 611px;
    height: 675px;
    overflow: hidden;
    color: var(--white);
  }
  .hero-backdrop {
    position: absolute;
    inset: 0;
    background: linear-gradient(155deg, var(--blue-deep) 0%, var(--blue-mid) 45%, var(--teal) 100%);
  }
  .brand-name {
    position: absolute;
    left: 185px;
    top: 38px;
    font-weight: 500;
    font-size: 20px;
    line-height: 1;
    color: var(--white);
  }
  .hero-title {
    position: absolute;
    left: 182px;
    top: 212px;
    font-weight: 500;
    font-size: 94px;
    line-height: 90px;
    letter-spacing: -2px;
  }
  .hero-lead {
    position: absolute;
    left: 185px;
    top: 422px;
    width: 350px;
    font-weight: 300;
    font-size: 18px;
    line-height: 22.5px;
  }
  .signin {
    position: absolute;
    left: 733px;
    top: 204px;
    width: 283px;
  }
  .signin-title {
    font-weight: 400;
    font-size: 38px;
    line-height: 1.2;
    color: var(--ink);
    letter-spacing: -0.3px;
  }
  .signin-rule {
    width: 52px;
    height: 3px;
    background: var(--accent);
    margin-top: 11px;
    margin-bottom: 24px;
  }
  .field {
    display: block;
    width: 283px;
    height: 41px;
    border: 1.5px solid var(--field-border);
    border-radius: 21px;
    padding: 0 29px;
    font-family: "Outfit", sans-serif;
    font-weight: 300;
    font-size: 12px;
    color: var(--ink);
    background: var(--white);
    outline: none;
  }
  .field::placeholder { color: var(--placeholder); }
  .field + .field { margin-top: 15px; }
  .cta {
    display: block;
    margin-top: 38px;
    width: 171px;
    height: 41px;
    border: none;
    border-radius: 21px;
    background: var(--accent);
    color: var(--white);
    font-family: "Outfit", sans-serif;
    font-weight: 600;
    font-size: 14.5px;
    cursor: pointer;
  }
</style>
</head>
<body>
  <main class="login-page">
    <section class="hero">
      <div class="hero-backdrop" role="img" aria-label="Photo of a person typing on a laptop at a desk, tinted in a blue to teal gradient"></div>
      <span class="brand-name">ORBIT Freight Lane</span>
      <h1 class="hero-title">Box It,<br>Move It.</h1>
      <p class="hero-lead">Lorem ipsum dolor sit amet, consectetur adipiscing elit, sed do eiusmod.</p>
    </section>

    <form class="signin" action="#">
      <h2 class="signin-title">Welcome Back</h2>
      <div class="signin-rule"></div>
      <input class="field" type="email" placeholder="Email Address" aria-label="Email Address">
      <input class="field" type="password" placeholder="Password" aria-label="Password">
      <button class="cta" type="submit">Contact Us now!</button>
    </form>
  </main>
</body>
</html>
```